Pediatric Speech Therapy Private Practice Announcement

I opened a solo private practice as a pediatric speech therapist in June 2014 in Orinda, CA in June 2014. I have 25 years experience in the field and worked as the Director of a very successful group practice of speech therapists in nearby Walnut Creek. I am trying to get my own name established in the local community and letting people know that I now have my own practice, which I call Halvery Speech-Language Center.

I would like this postcard to advertise low-cost speech-language screenings offered to nearby preschools.

Target Market(s)

Preschool Directors

Industry/Entity Type

Call

Requirements
Must have
• Photos of children, preschool ages, 3-5

Bright colors to get attention

```html
<!DOCTYPE html>
<html lang="en">
<head>
<meta charset="utf-8">
<title>Halvery Speech-Language Center – Postcard</title>
<link rel="stylesheet" href="https://fonts.googleapis.com/css2?family=Fira+Sans:ital,wght@1,900&family=Fira+Sans+Condensed:wght@400;500&family=Jost:wght@700&family=Open+Sans:wght@400&display=swap">
<style>
  :root {
    --backdrop: #e1e1e1;
    --navy: #27235f;
    --navy-light: #2f3a86;
    --red: #e21e26;
    --red-dark: #9c1420;
    --lime: #d9e021;
    --white: #ffffff;
    --ink-grey: #555555;
    --rule: #c8c8c8;
    --caption: #8a8a8a;
  }
  * { margin: 0; padding: 0; box-sizing: border-box; }
  html, body { width: 1200px; height: 1000px; overflow: hidden; }
  body { background: var(--backdrop); position: relative; font-family: "Fira Sans Condensed", sans-serif; }

  .postcard {
    position: absolute; left: 21px; top: 135px; width: 1156px; height: 665px;
    background: var(--white);
    box-shadow: 0 2px 8px rgba(0,0,0,0.35);
  }
  .promo-side {
    position: absolute; left: 0; top: 0; width: 756px; height: 665px;
    background: radial-gradient(ellipse at 55% 55%, var(--navy-light) 0%, var(--navy) 70%);
  }
  .ribbon { position: absolute; left: 47px; top: 0; width: 347px; height: 617px; filter: drop-shadow(3px 4px 6px rgba(0,0,0,0.45)); }
  .ribbon-text { position: absolute; left: 47px; top: 0; width: 347px; text-align: center; color: var(--white); }
  .headline-new {
    margin-top: 72px; font-family: "Fira Sans", sans-serif; font-style: italic; font-weight: 900;
    font-size: 78px; line-height: 1; color: var(--lime); letter-spacing: 1px;
    text-shadow: 2px 3px 4px rgba(0,0,0,0.4);
  }
  .headline-sub {
    margin-top: 8px; font-family: "Fira Sans", sans-serif; font-style: italic; font-weight: 900;
    font-size: 32px; line-height: 46px; text-transform: uppercase;
    text-shadow: 2px 3px 4px rgba(0,0,0,0.4);
  }
  .services {
    margin-top: 52px; font-size: 30px; line-height: 45px; font-weight: 400;
    text-shadow: 2px 2px 4px rgba(0,0,0,0.4);
  }
  .photo-children {
    position: absolute; left: 394px; top: 48px; width: 362px; height: 257px;
    background:
      radial-gradient(circle at 50% 45%, #f2d2b8 0%, rgba(242,210,184,0) 45%),
      linear-gradient(135deg, #3fb5c9 0%, #f3f3f3 45%, #d23a7a 65%, #8fc63c 100%);
  }
  .practice-info { position: absolute; left: 419px; top: 342px; color: var(--white); }
  .practice-name { font-family: "Jost", sans-serif; font-weight: 700; font-size: 19px; line-height: 26px; }
  .practitioner { font-size: 19px; line-height: 26px; }
  .phone { margin-top: 24px; font-family: "Jost", sans-serif; font-weight: 700; font-size: 27px; line-height: 30px; color: var(--lime); }
  .contact-line { font-size: 18px; line-height: 28px; }
  .contact-line:first-of-type { margin-top: 4px; }
  .hours-title { margin-top: 28px; font-family: "Jost", sans-serif; font-weight: 700; font-size: 19px; line-height: 28px; }
  .hours-line { font-size: 19px; line-height: 28px; }

  .mail-side { position: absolute; left: 756px; top: 0; width: 400px; height: 665px; }
  .return-address { position: absolute; left: 34px; top: 76px; font-family: "Open Sans", sans-serif; font-size: 14px; line-height: 23px; color: var(--ink-grey); }
  .stamp-box { position: absolute; left: 234px; top: 20px; width: 164px; height: 168px; border: 1px solid var(--rule); }
  .address-line { position: absolute; left: 55px; width: 330px; border-top: 1px solid var(--rule); }

  .format-caption {
    position: absolute; right: 33px; top: 832px; font-family: "Open Sans", sans-serif;
    font-size: 22px; color: var(--caption); letter-spacing: 0.5px;
  }
</style>
</head>
<body>
  <section class="postcard">
    <div class="promo-side">
      <svg class="ribbon" viewBox="0 0 347 617" aria-hidden="true">
        <defs>
          <radialGradient id="ribbonGlow" cx="50%" cy="55%" r="65%">
            <stop offset="0%" stop-color="#ed1c24"/>
            <stop offset="100%" stop-color="#9c1420"/>
          </radialGradient>
        </defs>
        <polygon points="0,0 347,0 347,617 173,513 0,617" fill="url(#ribbonGlow)"/>
      </svg>
      <div class="ribbon-text">
        <p class="headline-new">NEW</p>
        <h1 class="headline-sub">Pediatric Speech<br>Therapy Practice<br>in Orinda</h1>
        <p class="services">Speech, Language and<br>Social Communication<br>Therapy Services</p>
      </div>

      <div class="photo-children" role="img" aria-label="Photo of four smiling preschool children huddled in a circle looking down at the camera"></div>

      <div class="practice-info">
        <p class="practice-name">Halvery Speech-Language Center</p>
        <p class="practitioner">Maren Halvery, MS, CCC-SLP</p>
        <p class="phone">(925) 555-0148</p>
        <p class="contact-line">halveryspeechtherapy@mail.com</p>
        <p class="contact-line">www.halveryspeech-languagecenter.com</p>
        <p class="hours-title">Hours of Operation</p>
        <p class="hours-line">Mon - Fri: 8:30 - 6:30pm</p>
        <p class="hours-line">Sat - Sun: Closed</p>
      </div>
    </div>

    <div class="mail-side">
      <p class="return-address">14 Alder Ridge Way, #210<br>Orinda, CA&nbsp; 94563</p>
      <div class="stamp-box"></div>
      <div class="address-line" style="top:386px"></div>
      <div class="address-line" style="top:434px"></div>
      <div class="address-line" style="top:482px"></div>
      <div class="address-line" style="top:530px"></div>
    </div>
  </section>

  <p class="format-caption">US POSTCARD OVERSIZE BACK</p>
</body>
</html>
```